Partial Wrap Design for Painting Company

Need a wrap design that we can adapt to several vans. The immediate need is for 2016 Korvath LX300 and 2009 Varnel T-340. Vehicles are white.
We want a PARTIAL wrap (not full coverage).
We want to show;
- our phone number; (555) 274-QUIB
- our website address; www.quibpainting.com
- our services; Interior - Exterior - Cabinet
Any questions? Feel free to ask.

Target Market(s)

Homeowners

Industry/Entity Type

Painting

```html
<!DOCTYPE html>
<html lang="en">
<head>
<meta charset="UTF-8">
<title>Quib Painting – Partial Van Wrap</title>
<link rel="stylesheet" href="https://fonts.googleapis.com/css2?family=Montserrat:wght@500;700&family=Open+Sans:wght@600&display=swap">
<style>
  :root {
    --page: #ffffff;
    --wrap-white: #f7f7f2;
    --wrap-blue: #0f8fd6;
    --wrap-blue-deep: #0a6fb3;
    --accent-green: #9cc82a;
    --accent-orange: #f0900f;
    --brand-blue: #1d87c8;
    --text-light: #ffffff;
  }
  * { margin: 0; padding: 0; box-sizing: border-box; }
  html, body { width: 1200px; height: 1200px; overflow: hidden; background: var(--page); }
  .canvas { position: relative; width: 1200px; height: 1200px; }
  .wrap-panel {
    position: absolute; left: 100px; top: 220px; width: 1000px; height: 720px;
    border-radius: 28px; overflow: hidden; background: var(--wrap-white);
  }
  .wrap-shapes { position: absolute; inset: 0; width: 100%; height: 100%; }
  .brand {
    position: absolute; top: 120px; left: 0; width: 100%;
    text-align: center; color: var(--brand-blue);
    font-family: "Montserrat", sans-serif; font-weight: 700;
  }
  .brand-name { display: block; font-size: 150px; line-height: 1; letter-spacing: 4px; }
  .brand-trade { display: block; margin-top: 22px; font-size: 42px; line-height: 1; letter-spacing: 26px; padding-left: 26px; }
  .services {
    position: absolute; top: 500px; left: 0; width: 100%; text-align: center;
    font-family: "Open Sans", sans-serif; font-weight: 600; font-size: 46px;
    color: var(--text-light); letter-spacing: 0.5px;
  }
  .services .dot { color: var(--accent-orange); margin: 0 14px; font-size: 34px; vertical-align: 6px; }
  .contact {
    position: absolute; top: 578px; left: 0; width: 100%;
    display: flex; justify-content: center; align-items: center; gap: 26px;
    font-family: "Montserrat", sans-serif; font-weight: 500; font-size: 31px;
    color: var(--text-light);
  }
  .contact-item { display: flex; align-items: center; gap: 12px; }
  .contact-icon { width: 30px; height: 30px; }
</style>
</head>
<body>
<div class="canvas">
  <div class="wrap-panel">
    <svg class="wrap-shapes" viewBox="0 0 1000 720" preserveAspectRatio="none" aria-hidden="true">
      <defs>
        <linearGradient id="blueBand" x1="0" y1="0" x2="0" y2="1">
          <stop offset="0" stop-color="var(--wrap-blue)"/>
          <stop offset="1" stop-color="var(--wrap-blue-deep)"/>
        </linearGradient>
      </defs>
      <path d="M0,370 Q500,620 1000,370 L1000,720 L0,720 Z" fill="url(#blueBand)"/>
      <path d="M0,290 C150,400 330,480 480,500 C330,492 150,432 0,368 Z" fill="var(--accent-green)"/>
      <path d="M1000,262 C850,380 690,468 545,497 C700,482 860,424 1000,340 Z" fill="var(--accent-orange)"/>
    </svg>

    <div class="brand">
      <span class="brand-name">QUIB</span>
      <span class="brand-trade">PAINTING</span>
    </div>

    <p class="services">INTERIOR<span class="dot">•</span>EXTERIOR<span class="dot">•</span>CABINET</p>

    <div class="contact">
      <span class="contact-item">
        <svg class="contact-icon" viewBox="0 0 24 24" aria-hidden="true">
          <path fill="var(--accent-orange)" d="M6.6 10.8a15.1 15.1 0 0 0 6.6 6.6l2.2-2.2a1 1 0 0 1 1-.25 11.4 11.4 0 0 0 3.6.57 1 1 0 0 1 1 1V20a1 1 0 0 1-1 1A17 17 0 0 1 3 4a1 1 0 0 1 1-1h3.5a1 1 0 0 1 1 1c0 1.25.2 2.45.57 3.57a1 1 0 0 1-.25 1z"/>
        </svg>
        (555) 274-QUIB
      </span>
      <span class="contact-item">
        <svg class="contact-icon" viewBox="0 0 24 24" aria-hidden="true">
          <g fill="none" stroke="var(--accent-orange)" stroke-width="1.6">
            <circle cx="12" cy="12" r="9.5"/>
            <ellipse cx="12" cy="12" rx="4.2" ry="9.5"/>
            <line x1="2.5" y1="12" x2="21.5" y2="12"/>
            <path d="M4 7h16M4 17h16"/>
          </g>
        </svg>
        www.quibpainting.com
      </span>
    </div>
  </div>
</div>
</body>
</html>
```